Tranquil Harbour Hypnotherapy 2017 DL Card Flyer

We would like a double sided DL Card Flyer design.

We are a professional Hypnotherapy Clinic looking for a fresh clean design.

Front of card is summary info and back of flyer is detailed text.

I have attached documents with text for the front (dl size hypno 1) and back (dl size hypno 2) of the card and an indicative style of layout.

There are logo files uploaded as well as one image file.

The colors we like are blue, white and yellow/gold.
Updates

please note: when using the 'new mindset new results' image, please only use the top half of the image. The girl is not to be in the image, just the words and light bulb with the chalk underline. thanks.. Added Sunday, March 19, 2017

Industry/Entity Type

Health And Wellness

Requirements
Must have
• Note. I have misspelled the www.TranquilHarbourHypnotherapy.com.au (missing an 'o' in the attachments to the brief). My error. Please amend in your design submissions.

```html
<!DOCTYPE html>
<html lang="en">
<head>
<meta charset="utf-8">
<title>Tranquil Harbour Hypnotherapy – DL Flyer</title>
<link href="https://fonts.googleapis.com/css2?family=Hind:wght@400;500;600;700&family=Playball&family=Catamaran:wght@600;700&display=swap" rel="stylesheet">
<style>
  :root {
    --navy: #232c6b;
    --gold: #e5c61f;
    --gold-dark: #c2a633;
    --session: #f2d51c;
    --paper: #f4f4f4;
    --body-text: #eef0f6;
    --backdrop: #dcdcdc;
    --chalk: #3a3a3a;
  }
  * { box-sizing: border-box; margin: 0; padding: 0; }
  html, body { width: 1200px; height: 1200px; overflow: hidden; }
  body {
    background: radial-gradient(circle at 50% 45%, #ececec 0%, var(--backdrop) 100%);
    font-family: "Hind", sans-serif;
    position: relative;
  }
  .panel {
    position: absolute;
    top: 153px;
    width: 433px;
    height: 917px;
    box-shadow: 0 2px 8px rgba(0,0,0,.18);
    overflow: hidden;
  }
  /* ---------- front ---------- */
  .front { left: 118px; background: var(--paper); }
  .brand {
    position: absolute; top: 16px; left: 0; width: 100%; height: 110px;
    display: flex; align-items: center; justify-content: center; gap: 16px;
  }
  .brand-dot { width: 90px; height: 90px; border-radius: 50%; background: var(--navy); flex: none; }
  .brand-name {
    font-weight: 700; color: var(--navy); font-size: 28px; line-height: 1.05;
  }
  .rule { position: absolute; background: var(--navy); }
  .front-body {
    position: absolute; top: 163px; left: 0; width: 100%; height: 688px; background: var(--navy);
  }
  .front-body > * { position: absolute; }
  .quote {
    top: 24px; left: 0; width: 100%; text-align: center;
    font-family: "Playball", cursive; color: #fff; font-size: 27px; line-height: 33px;
  }
  .mindset-art {
    top: 116px; left: 0; width: 100%; height: 230px;
    background: radial-gradient(ellipse at 50% 55%, #4d4d47 0%, var(--chalk) 60%, #303030 100%);
  }
  .programs-title {
    top: 362px; left: 0; width: 100%; text-align: center;
    color: #fff; font-weight: 600; font-size: 19.5px; line-height: 28px;
  }
  .ornament { top: 398px; left: 162px; }
  .program-list { top: 416px; left: 33px; list-style: none; }
  .program-list li {
    color: #fff; font-size: 19.5px; height: 33px; line-height: 33px;
    display: flex; align-items: center;
  }
  .program-list li::before {
    content: ""; width: 14px; height: 14px; background: var(--gold);
    transform: rotate(45deg); margin: 0 22px 0 6px; flex: none;
  }
  .call-line { top: 612px; height: 2px; background: #fff; width: 128px; }
  .call-banner {
    top: 596px; left: 156px; width: 121px; height: 33px; background: #fff;
    clip-path: polygon(0 0, 100% 0, 94% 50%, 100% 100%, 0 100%, 6% 50%);
    text-align: center; line-height: 36px; color: var(--navy);
    font-family: "Catamaran", sans-serif; font-weight: 700; font-variant: small-caps; font-size: 21px;
  }
  .phone {
    top: 643px; left: 0; width: 100%; display: flex; justify-content: center; align-items: center; gap: 12px;
    color: #fff; font-weight: 600; font-size: 21px; line-height: 30px;
  }
  .website {
    position: absolute; top: 877px; left: 0; width: 100%;
    display: flex; justify-content: center; align-items: center; gap: 7px;
    color: var(--navy); font-weight: 700; font-size: 16px; line-height: 24px;
  }
  /* ---------- back ---------- */
  .back { left: 649px; background: var(--navy); }
  .back-title {
    position: absolute; top: 14px; left: 0; width: 100%;
    display: flex; justify-content: center; align-items: center; gap: 12px;
    color: #fff; font-family: "Catamaran", sans-serif; font-weight: 700; font-variant: small-caps; font-size: 21px;
  }
  .program { position: absolute; left: 0; width: 100%; }
  .program-head {
    height: 31px; line-height: 33px; background: var(--gold); color: var(--navy);
    font-weight: 600; font-size: 14.5px; position: relative; white-space: nowrap;
  }
  .program-head.left { width: 360px; border-radius: 0 16px 16px 0; padding-left: 28px; }
  .program-head.left::before {
    content: ""; position: absolute; left: 0; top: 0; width: 26px; height: 100%; background: var(--gold-dark);
  }
  .program-head.right { margin-left: 53px; border-radius: 16px 0 0 16px; padding-left: 19px; }
  .program-head.right::after {
    content: ""; position: absolute; right: 0; top: 0; width: 24px; height: 100%; background: var(--gold-dark);
  }
  .program-head small { font-size: 12px; }
  .program-text {
    margin: 10px 24px 0 26px; color: var(--body-text); font-size: 14px; line-height: 18.4px;
    text-align: justify;
  }
  .sessions { margin-left: 26px; color: var(--session); font-style: italic; font-weight: 500; font-size: 13.6px; line-height: 19px; }
  .cd-note {
    position: absolute; top: 837px; left: 16px; width: 400px; height: 56px;
    border: 1.5px solid #fff; color: #fff; font-style: italic; font-size: 13.6px; line-height: 18.5px;
    text-align: center; padding-top: 9px;
  }
</style>
</head>
<body>

<section class="panel front" aria-label="Flyer front">
  <div class="brand">
    <span class="brand-dot"></span>
    <div class="brand-name">Tranquil Harbour<br>Hypnotherapy</div>
  </div>
  <div class="rule" style="top:141px;left:27px;width:381px;height:8px"></div>
  <div class="rule" style="top:151px;left:13px;width:408px;height:9px"></div>

  <div class="front-body">
    <p class="quote">“There is nothing more important<br>than good health”</p>
    <div class="mindset-art" role="img" aria-label="Chalkboard illustration: glowing light bulb between the words New Mindset and New Results with a dashed arrow"></div>
    <h2 class="programs-title">Professional Hypnosis Therapy Programs</h2>
    <svg class="ornament" width="110" height="8" viewBox="0 0 110 8" aria-hidden="true">
      <path d="M0 4 Q30 2 55 4 Q80 2 110 4 Q80 6 55 4 Q30 6 0 4Z" fill="#e5c61f" stroke="#e5c61f" stroke-width="1.2"/>
      <circle cx="55" cy="4" r="3.5" fill="#e5c61f"/>
    </svg>
    <ul class="program-list">
      <li>Weight Loss &nbsp;&nbsp;(Virtual Gastric Band)</li>
      <li>Sugar Addiction</li>
      <li>Quit Smoking</li>
      <li>Chronic Fatigue &amp; Chronic Pain Relief</li>
      <li>Stress Relief &amp; Deep Relaxation</li>
    </ul>
    <div class="call-line" style="left:24px"></div>
    <div class="call-line" style="left:281px"></div>
    <div class="call-banner">Call Us</div>
    <div class="phone">
      <svg width="26" height="26" viewBox="0 0 26 26" aria-hidden="true">
        <circle cx="13" cy="13" r="12" fill="#fff"/>
        <path d="M9 7 l3 0 1 4 -2 1.5 q1.5 3 4 4 l1.5 -2 4 1 0 3 q-1 1.5 -3 1 q-8 -2.5 -9.5 -10.5 q-0.5 -1.5 1 -2Z" fill="#232c6b"/>
      </svg>
      <span>1300 555 014</span>
    </div>
  </div>

  <div class="rule" style="top:853px;left:13px;width:408px;height:8px"></div>
  <div class="rule" style="top:864px;left:27px;width:381px;height:7px"></div>
  <div class="website">
    <svg width="20" height="20" viewBox="0 0 20 20" aria-hidden="true">
      <circle cx="10" cy="10" r="8.5" fill="none" stroke="#232c6b" stroke-width="2"/>
      <ellipse cx="10" cy="10" rx="3.5" ry="8.5" fill="none" stroke="#232c6b" stroke-width="1.6"/>
      <path d="M2 10h16M3.5 6h13M3.5 14h13" stroke="#232c6b" stroke-width="1.4"/>
    </svg>
    <span>www.TranquilHarbourHypnotherapy.com.au</span>
  </div>
  <div class="rule" style="top:907px;left:0;width:100%;height:10px"></div>
</section>

<section class="panel back" aria-label="Flyer back">
  <h2 class="back-title">
    <svg width="62" height="10" viewBox="0 0 62 10" aria-hidden="true"><path d="M0 5 L54 3.5 L54 6.5Z" fill="#e5c61f"/><circle cx="57" cy="5" r="4" fill="#e5c61f"/></svg>
    Program Details
    <svg width="62" height="10" viewBox="0 0 62 10" aria-hidden="true"><circle cx="5" cy="5" r="4" fill="#e5c61f"/><path d="M8 3.5 L62 5 L8 6.5Z" fill="#e5c61f"/></svg>
  </h2>

  <article class="program" style="top:53px">
    <h3 class="program-head left">WEIGHT LOSS PROGRAM (V<small>IRTUAL</small> G<small>ASTRIC</small> B<small>AND</small>)</h3>
    <p class="program-text">Achieve long term weight loss without dieting. Whether it’s losing 3kg or 30kg, we’ll help you become the shape and size you want to be. Our Internationally Accredited Program is proven to be 95% effective in clinical trials.</p>
    <p class="sessions">Number of Sessions: 6+</p>
  </article>

  <article class="program" style="top:196px">
    <h3 class="program-head right">SUGAR ADDICTION PROGRAM</h3>
    <p class="program-text">Excess sugar intake can lead to obesity, Type 2 Diabetes and tooth decay. The habit of reaching for soft drinks, chocolate, sweets, cakes and biscuits can be hard to break. By rewiring your subconscious habits, our Program puts you back in control.</p>
    <p class="sessions">Number of Sessions: 3+</p>
  </article>

  <article class="program" style="top:354px">
    <h3 class="program-head left" style="width:352px">QUIT SMOKING PROGRAM</h3>
    <p class="program-text">The facts speak for themselves. You are 10 times more likely to quit smoking for good using hypnotherapy. Expect to be a non smoker after completing the first session of our Program. (12 Month Guarantee)</p>
    <p class="sessions">Number of Sessions: 2</p>
  </article>

  <article class="program" style="top:494px">
    <h3 class="program-head right" style="padding-left:7px;font-size:14px">CHRONIC FATIGUE &amp; CHRONIC PAIN RELIEF PROGRAM</h3>
    <p class="program-text">Chronic Fatigue, Fibromyalgia and Chronic Musculoskeletal Pain are diseases of modern living. The symptoms of fatigue and pain are very real, however the cause is usually emotional, and is generally hidden beyond our conscious awareness. Our Program comprises Education and Hypnosis to help you regain your health, your self esteem, your friends and your life, all in a manageable timeframe.</p>
    <p class="sessions">Number of Sessions: 6+</p>
  </article>

  <article class="program" style="top:689px">
    <h3 class="program-head left" style="width:352px">STRESS RELIEF &amp; DEEP RELAXATION PROGRAM</h3>
    <p class="program-text">Our Program gently uncovers the true source of your stress, and helps you reconnect to a natural inner calm. We teach you self hypnosis so that you have the tools to continue your experience.</p>
    <p class="sessions">Number of Sessions: 3+</p>
  </article>

  <p class="cd-note">All Programs include take home CD’s personally recorded<br>by our therapists, using advanced hypnotic techniques.</p>
</section>

</body>
</html>
```